■依頼の概要
子どもの結婚を望む親御様に向けた電子書籍(pagora出版)の表紙デザイン作成をお願いします。
電子書籍なので、タイトルがはっきり分かるものでお願いします。

■本のタイトル
いつか、わが家にも春は来るだろうか? ~家族の未来をひらく手引き~

■本の内容
子どもの結婚を望む親御様に向けて、今どきの婚活・結婚事情をデータでご紹介している他、婚活成就するための考え方や事例を紹介しています。
原稿内容を添付します。

■読者ターゲット
息子・娘に結婚してほしいと願っている親御様
(20代~50代位の独身のお子さんに結婚してほしいと願っている親御様・子どもの結婚のためなら何でもする覚悟の親御様・親子関係が良好ではない親御様)

■デザイン要望
原稿内容を参考にしていただいて、より売れることを目的としたデザインにしてください。
デザイナーさんのパフォーマンスを引き出したいので、デザイナーさんのセンスにお任せします。

■その他
Zuvomiの利用が不慣れなためアクション方法が分からず、対応がスマートでない場合はご指摘・ご教示いただけますと助かります。
何かご不明な点がございましたら、お気軽にご質問ください。
尚、最終的には私が籍を置く出版スクール内での投票で、一番人気のあったデザインに決めさせていただきます。

以上、何卒宜しくお願い申し上げます。
【ご提案をいただいた皆様へ】

この度はステキな表紙デザインを数多くご提案いただきまして、本当にありがとうございます。
皆様からいただきましたご提案は、私が籍を置く出版スクール内でのルールで、デザインの人気投票を行い一番得票数の多かったデザインを採用させていただきます。
それ故、締め切り後しばらくお時間をいただきますが、表紙をお願いしたい方には後日ご連絡をさせていただきます。
尚、全員の方お一人お一人にお礼のご挨拶ができませんことお許しいただき、この場でのご挨拶とさせていただきます。
この度の皆様からのご提案に心から感謝申し上げます。
ありがとうございましたm(__)m

皆様からご提案をいただきまして、私が籍を置く出版スクール内で表紙デザインの人気投票を行いました(これが、出版スクールでの標準的ルールになっています)
そうしましたところ、こちらのデザインに一番票が集まりました。
ご投票いただいた方々のコメントには、親の気持ちがそのままデザインに表されている・タイトルがスッと目に入ってきた・優しいピンクが、焦燥感を和らげてる・水引に縁起の良さを感じるなどたくさんのコメントをいただきました。

この度は、皆様からたくさんのご提案をいただきまして、本当にありがとうございましたm(__)m
素晴らしい作品に恵まれ、また私の好みをお伝えさせていただいた際には、皆様快く修正や追加提案をいただいて、また迅速にご対応いただいて、本当に有難く感謝の気持ちでいっぱいでおります。
これだけたくさんの、しかも素晴らしいご提案をいただいたら私自身もどれにしようか悩んでしまいました。
最終的には、人気投票で一番人気のデザインに決めさせていただきました。
この度のコンペにご参加の全ての皆様に心から感謝申し上げます。

```html
<!DOCTYPE html>
<html lang="ja">
<head>
<meta charset="UTF-8">
<title>いつか、わが家にも春は来るだろうか？ 表紙</title>
<link href="https://fonts.googleapis.com/css2?family=Noto+Sans+JP:wght@400;500;700;900&display=swap" rel="stylesheet">
<style>
  :root {
    --paper: #ffffff;
    --navy: #2b3552;
    --pink: #e8607e;
    --teal: #35b3a6;
    --teal-deep: #2a9d91;
    --mother-tone: #f6d7da;
    --son-tone: #d8e6f3;
  }
  html, body { margin: 0; padding: 0; overflow: hidden; background: var(--paper); }
  p, h1 { margin: 0; }
  .cover {
    position: relative;
    width: 752px; height: 1200px;
    overflow: hidden;
    background: var(--paper);
    font-family: "Noto Sans JP", sans-serif;
    color: var(--navy);
  }
  .portrait { position: absolute; border-radius: 50%; }
  .portrait--mother {
    left: 35px; top: 55px; width: 200px; height: 200px;
    background: radial-gradient(circle at 50% 40%, #fbe6e8, var(--mother-tone));
  }
  .portrait--son {
    left: 420px; top: 560px; width: 150px; height: 150px;
    background: radial-gradient(circle at 50% 40%, #e9f1f9, var(--son-tone));
  }
  .title-line {
    position: absolute;
    right: 34px;
    font-weight: 900;
    line-height: 1;
    white-space: nowrap;
    text-align: right;
  }
  .title-line--1 { top: 40px; font-size: 100px; }
  .title-line--2 { top: 165px; font-size: 70px; }
  .title-line--2 .accent { font-size: 82px; }
  .title-line--3 { top: 262px; font-size: 104px; }
  .title-line--4 { top: 390px; font-size: 70px; }
  .accent { color: var(--pink); }
  .subtitle {
    position: absolute;
    top: 268px;
    writing-mode: vertical-rl;
    color: var(--teal-deep);
    font-weight: 700;
    font-size: 38px;
    line-height: 1;
  }
  .subtitle--a { left: 250px; }
  .subtitle--b { left: 200px; }
  .author-role {
    position: absolute;
    left: 664px; top: 492px;
    writing-mode: vertical-rl;
    font-size: 20px; font-weight: 700; line-height: 1;
  }
  .author-name {
    position: absolute;
    left: 596px; top: 560px;
    writing-mode: vertical-rl;
    font-size: 44px; font-weight: 900; line-height: 1;
  }
  .author-ruby {
    position: absolute;
    left: 644px; top: 566px;
    writing-mode: vertical-rl;
    font-size: 13px; font-weight: 500; line-height: 1;
  }
  .band {
    position: absolute;
    left: 0; top: 826px;
    width: 752px; height: 374px;
    background: var(--teal);
  }
  .band-headline {
    position: absolute;
    left: 34px; top: 34px;
    color: #fff;
    font-size: 62px; font-weight: 900; line-height: 1.22;
  }
  .gift {
    position: absolute;
    left: 506px; top: 26px;
    width: 216px; height: 168px;
    background: #fff;
    border-radius: 14px;
    text-align: center;
    box-sizing: border-box;
    padding-top: 18px;
  }
  .gift-label { color: var(--pink); font-size: 34px; font-weight: 900; line-height: 1.15; }
  .gift-text { margin-top: 10px; color: var(--navy); font-size: 19px; font-weight: 700; line-height: 1.35; }
  .band-lead {
    position: absolute;
    left: 34px; top: 228px;
    color: #fff;
    font-size: 31px; font-weight: 700; line-height: 1.6;
  }
</style>
</head>
<body>
  <div class="cover">
    <div class="portrait portrait--mother" role="img" aria-label="微笑む母親のイラスト"></div>
    <div class="portrait portrait--son" role="img" aria-label="スーツ姿の息子のイラスト"></div>

    <h1 class="title">
      <span class="title-line title-line--1">いつか、</span>
      <span class="title-line title-line--2">わが<span class="accent">家</span>にも</span>
      <span class="title-line title-line--3"><span class="accent">春</span>は来る</span>
      <span class="title-line title-line--4">だろうか？</span>
    </h1>

    <p class="subtitle subtitle--a">家族の未来を</p>
    <p class="subtitle subtitle--b">ひらく手引き</p>

    <p class="author-role">家族縁むすびアドバイザー</p>
    <p class="author-ruby">うた</p>
    <p class="author-name">詩 まどか</p>

    <section class="band">
      <p class="band-headline">悩んだらまず、<br>読んでほしい</p>
      <div class="gift">
        <div class="gift-label">読者<br>プレゼント</div>
        <div class="gift-text">運命の人に出会う<br>方法を診断!</div>
      </div>
      <p class="band-lead">今どきの婚活・結婚事情から<br>婚活成就するための考え方や事例を紹介</p>
    </section>
  </div>
</body>
</html>
```